Clinical Hypnotherapist needs business card design

I need a business card design that gives the impression of being approachable yet professional. As a clinical hypnotherapist I need to create trust from my clients to allow me access to their inner mind to enable them to make changes and to start to live the life that they want to live. My website is www.lunarelle.com.au and I would like my business cards to reflect my website. I would like a space for appointment details on the back of the card.

```html
<!DOCTYPE html>
<html lang="en">
<head>
<meta charset="utf-8">
<title>Clara Wrenfield – Business Card</title>
<link href="https://fonts.googleapis.com/css2?family=Marck+Script&family=Tinos&display=block" rel="stylesheet">
<style>
  :root {
    --plum-deep: #2a0a26;
    --plum: #4a1543;
    --plum-mid: #5e1c56;
    --plum-light: #7a2d70;
    --photo-top: #b58ccb;
    --photo-bottom: #8a4a6e;
    --ink: #2b1a28;
    --paper: #ffffff;
    --rule: #e6dfe5;
    --text-light: #f4eef3;
    --text-soft: #d9c9d6;
    --backdrop: #e9e7ea;
  }
  * { margin: 0; padding: 0; box-sizing: border-box; }
  html, body { width: 1200px; height: 1000px; overflow: hidden; }
  body {
    background: var(--backdrop);
    font-family: "Tinos", "Times New Roman", serif;
    position: relative;
  }
  .card {
    position: absolute;
    box-shadow: 0 8px 24px rgba(0,0,0,0.18);
    overflow: hidden;
  }
  .script { font-family: "Marck Script", "Brush Script MT", cursive; }

  /* Front */
  .card-front {
    left: 98px; top: 328px;
    width: 600px; height: 343px;
    background: linear-gradient(160deg, var(--plum-mid) 0%, var(--plum) 45%, var(--plum-deep) 100%);
  }
  .card-front .photo-area { position: absolute; left: 0; top: 0; width: 600px; height: 343px; }
  .front-title {
    position: absolute; left: 200px; top: 122px; width: 370px;
    text-align: right;
  }
  .front-title .title-band {
    position: absolute; left: 10px; right: -30px; top: 8px; height: 58px;
    background: linear-gradient(90deg, rgba(255,255,255,0) 0%, rgba(255,255,255,0.12) 50%, rgba(255,255,255,0) 100%);
  }
  .front-title .name {
    position: relative;
    font-size: 56px; color: var(--text-light);
    line-height: 1.15;
  }
  .front-title .role {
    position: relative;
    font-size: 27px; color: var(--text-soft);
    margin-top: 2px; letter-spacing: 0.5px;
  }
  .front-web {
    position: absolute; left: 0; right: 0; bottom: 0; height: 62px;
    background: linear-gradient(180deg, var(--plum) 0%, var(--plum-deep) 100%);
    border-top: 1px solid rgba(255,255,255,0.12);
    display: flex; align-items: center; padding-left: 56px;
    font-size: 29px; color: var(--text-light); letter-spacing: 0.5px;
  }

  /* Back */
  .card-back {
    left: 758px; top: 200px;
    width: 343px; height: 600px;
    background: var(--paper);
  }
  .back-head {
    position: absolute; left: 0; top: 0; width: 100%; height: 132px;
    background: linear-gradient(180deg, var(--plum-light) 0%, var(--plum) 60%, var(--plum-deep) 100%);
    text-align: center;
  }
  .back-head .name {
    font-size: 44px; color: var(--text-light);
    padding-top: 26px; line-height: 1.15;
  }
  .back-head .role-band {
    margin: 4px 24px 0;
    background: linear-gradient(90deg, rgba(255,255,255,0) 0%, rgba(255,255,255,0.16) 50%, rgba(255,255,255,0) 100%);
    font-size: 19px; color: var(--text-soft); padding: 4px 0;
  }
  .appointment {
    position: absolute; left: 0; top: 132px; width: 100%; height: 300px;
    padding: 24px 30px 0;
    color: var(--ink);
  }
  .appointment .label { font-size: 21px; text-align: center; }
  .appointment .write-line { height: 36px; border-bottom: 1px solid var(--rule); }
  .appointment .notice {
    position: absolute; left: 0; right: 0; top: 204px;
    text-align: center; font-size: 18px; line-height: 1.25;
    text-transform: uppercase;
  }
  .back-foot {
    position: absolute; left: 0; bottom: 0; width: 100%; height: 168px;
    background: radial-gradient(ellipse at 50% 60%, var(--plum-deep) 0%, var(--plum) 55%, var(--plum-mid) 100%);
    text-align: center; color: var(--text-light);
    padding-top: 56px;
  }
  .back-foot .phone { font-size: 22px; letter-spacing: 0.5px; }
  .back-foot .email { font-size: 18px; margin-top: 8px; color: var(--text-soft); }
</style>
</head>
<body>

<section class="card card-front">
  <svg class="photo-area" viewBox="0 0 600 343" role="img" aria-label="Photograph of a sunset over the ocean">
    <defs>
      <linearGradient id="photo-tone" x1="0" y1="0" x2="0" y2="1">
        <stop offset="0" stop-color="var(--photo-top)"/>
        <stop offset="1" stop-color="var(--photo-bottom)"/>
      </linearGradient>
    </defs>
    <path d="M0 0 H600 V14 C430 84 250 120 0 100 Z" fill="url(#photo-tone)"/>
    <path d="M0 100 C250 120 430 84 600 14 V40 C440 110 260 150 0 118 Z" fill="#3a0f35"/>
    <path d="M0 118 C260 150 440 110 600 40 V56 C430 126 240 170 0 150 Z" fill="rgba(255,255,255,0.06)"/>
  </svg>

  <div class="front-title">
    <div class="title-band"></div>
    <div class="name script">Clara Wrenfield</div>
    <div class="role">clinical hypnotherapist</div>
  </div>

  <div class="front-web">www.lunarelle.com.au</div>
</section>

<section class="card card-back">
  <header class="back-head">
    <div class="name script">Clara Wrenfield</div>
    <div class="role-band">clinical hypnotherapist</div>
  </header>

  <div class="appointment">
    <div class="label">Your appointment</div>
    <div class="write-line"></div>
    <div class="write-line"></div>
    <div class="write-line"></div>
    <div class="write-line"></div>
    <p class="notice">If you are unable<br>to keep appointment<br>please call</p>
  </div>

  <footer class="back-foot">
    <div class="phone">0400 162 539</div>
    <div class="email">clara@lunarelle.com.au</div>
  </footer>
</section>

</body>
</html>
```